Business Card Design for a new Senior Concierge Business 1.3.24

I need a professional business card to handout at networking events for my senior helper business. I would like to use the logo I have uploaded. The design should be clear and easy to read and should list the following information...
Dessa Kirwin
Owner
www.BrightwellElderAides.example
Alder Bend, Northvale
555.248.3906
Dessa@brightwellelderaides.example

Target Market(s)

Senior Citizens

Industry/Entity Type

Personal Helper/ Assisstant

Contact Information for Business Card

I have included the details in the project description box.

Font styles to use
Serif

Colors
0054AA
0677BA
7BADD7
CADEEF
E8F1F8
59FF00
82FF00
B8FF75
E3FFCB
F4FFEA
E54698
E96AAD
F1A4CE
F9D9EA
FCEFF6
6B429C
8869AF
B7A5CE
E3DAEB
F3F0F8

Requirements
Must have
• Include uploaded logo
Nice to have
• The log that has been uploaded
Should not have
• No crazy fonts

```html
<!DOCTYPE html>
<html lang="en">
<head>
<meta charset="utf-8">
<title>Brightwell Elder Aides – Business Card</title>
<link href="https://fonts.googleapis.com/css2?family=Montserrat:wght@800&family=Open+Sans:wght@400;600&display=swap" rel="stylesheet">
<style>
  :root {
    --stage: #232323;
    --card: #232226;
    --pink: #e01e5f;
    --teal: #16939c;
    --purple: #6b52b0;
    --white: #ffffff;
  }
  * { box-sizing: border-box; margin: 0; padding: 0; }
  html, body { width: 1200px; height: 779px; overflow: hidden; background: var(--stage); }
  .stage {
    position: relative; width: 1200px; height: 779px;
    display: flex; align-items: center; justify-content: center; gap: 40px;
  }
  .card {
    position: relative; width: 560px; height: 320px;
    background: var(--card); overflow: hidden;
    box-shadow: 0 14px 30px rgba(0,0,0,.55);
  }
  /* back */
  .card-back__pattern {
    position: absolute; inset: 0;
    background: linear-gradient(150deg, #1b1a1d 0%, #2a292d 45%, #3a393d 70%, #1e1d20 100%);
  }
  .card-back__brand {
    position: absolute; right: 40px; top: 150px;
    font-family: "Open Sans", sans-serif; font-weight: 400;
    font-size: 22px; line-height: 1.1; color: var(--purple);
  }
  /* front */
  .card-front__waves { position: absolute; inset: 0; width: 100%; height: 100%; }
  .card-front__accent {
    position: absolute; top: 0; right: 10px; width: 18px; height: 44px; background: var(--teal);
  }
  .holder { position: absolute; top: 16px; right: 36px; text-align: right; }
  .holder__name {
    font-family: "Montserrat", sans-serif; font-weight: 800; font-size: 25px; letter-spacing: .5px;
  }
  .holder__first { color: var(--teal); }
  .holder__last { color: var(--pink); }
  .holder__role {
    font-family: "Open Sans", sans-serif; font-weight: 600; font-size: 12px; color: var(--white);
    margin-top: 2px;
  }
  .brand {
    position: absolute; left: 30px; top: 84px;
    display: flex; align-items: center; gap: 10px;
    font-family: "Open Sans", sans-serif; font-weight: 400; color: var(--purple);
  }
  .brand__dot { width: 16px; height: 16px; border-radius: 50%; background: var(--purple); }
  .brand__name { font-size: 30px; line-height: 1; }
  .contact {
    position: absolute; left: 60px; top: 176px;
    font-family: "Open Sans", sans-serif; font-size: 12.5px; color: var(--white); line-height: 1.5;
    list-style: none;
  }
  .contact__city { margin-bottom: 8px; }
  .contact li { display: flex; align-items: center; gap: 8px; }
  .contact svg { width: 11px; height: 11px; flex: none; }
</style>
</head>
<body>
<main class="stage">

  <section class="card card-back" aria-label="Card back">
    <div class="card-back__pattern" role="img" aria-label="Tone-on-tone heart pattern with glossy sheen"></div>
    <p class="card-back__brand">Brightwell<br>Elder Aides</p>
  </section>

  <section class="card card-front" aria-label="Card front">
    <svg class="card-front__waves" viewBox="0 0 560 320" preserveAspectRatio="none" aria-hidden="true">
      <path fill="var(--pink)" d="M0,276 C190,292 300,220 375,168 C440,124 500,108 560,100 L560,320 L0,320 Z"/>
      <path fill="var(--card)" d="M0,285 C195,299 305,228 380,177 C444,133 502,118 560,110 L560,320 L0,320 Z"/>
      <path fill="var(--teal)" d="M0,291 C200,304 310,234 384,183 C446,140 504,126 560,118 L560,320 L0,320 Z"/>
    </svg>

    <div class="card-front__accent"></div>

    <header class="holder">
      <p class="holder__name"><span class="holder__first">Dessa</span> <span class="holder__last">Kirwin</span></p>
      <p class="holder__role">Owner</p>
    </header>

    <div class="brand">
      <span class="brand__dot"></span>
      <span class="brand__name">Brightwell Elder Aides</span>
    </div>

    <ul class="contact">
      <li class="contact__city">Alder Bend, Northvale</li>
      <li>
        <svg viewBox="0 0 12 12"><path fill="var(--teal)" d="M2.5 1 L4.5 3.2 L3.5 4.5 C4.2 6 5.9 7.7 7.5 8.5 L8.8 7.5 L11 9.5 L9.8 11 C5.5 10.6 1.4 6.5 1 2.2 Z"/></svg>
        555.248.3906
      </li>
      <li>
        <svg viewBox="0 0 12 12"><circle cx="6" cy="6" r="5" fill="none" stroke="var(--teal)" stroke-width="1.4"/><path d="M1 6 H11 M6 1 C3.5 4 3.5 8 6 11 M6 1 C8.5 4 8.5 8 6 11" fill="none" stroke="var(--teal)" stroke-width="1"/></svg>
        www.BrightwellElderAides.example
      </li>
      <li>
        <svg viewBox="0 0 12 12"><rect x="1" y="2.5" width="10" height="7" fill="none" stroke="var(--teal)" stroke-width="1.4"/><path d="M1 2.5 L6 7 L11 2.5" fill="none" stroke="var(--teal)" stroke-width="1.2"/></svg>
        Dessa@brightwellelderaides.example
      </li>
    </ul>
  </section>

</main>
</body>
</html>
```